Redesign web application

we are a tele health start up. we need a new design for our platform that allows users, their family and docs to access their detailed stats online
users take readings using our wireless devices that transmit the readings to our server in the background All this happens in real time . and users can instantly login to the portal to view readings , make comments, , view charts,
if readings are not within in prescribed thresholds then alerts are reported on the website, SMS and email
please see the screenshots of existing pages
We need the following pages re designed
login page
patient DB summary , patient DB condition
Doc DB
Nurse DB
After you submit designs and we choose the winning design . please help to make minor modifications after that so that we can use it
Target Market(s)
Paying
Doctors/ Clinics/Clinic chains/ Specialists will be the ones who are paying for the service. the service
Non Paying
patients family members, doctors all will be accessing the system to view readings, alerts , make comments , see charts
Industry/Entity Type
Health
Colors
Designer to choose colors to be used in the design.
Look and feel

```html
<!DOCTYPE html>
<html lang="en">
<head>
<meta charset="utf-8">
<title>Vital Beacon – Login</title>
<link rel="stylesheet" href="https://fonts.googleapis.com/css2?family=Open+Sans:wght@400;600&display=swap">
<style>
:root{
  --blue:#0a56b0;
  --blue-dark:#084b9e;
  --green:#6cbb2c;
  --green-light:#a5dc6c;
  --green-text:#6aae22;
  --ink:#222;
  --muted:#666;
  --field:#e6f4d6;
  --rule:#d9d9d9;
}
*{box-sizing:border-box;margin:0;padding:0}
html,body{width:960px;height:1200px;overflow:hidden;background:#fff}
body{font-family:"Open Sans",Arial,sans-serif;color:var(--ink);position:relative}
.abs{position:absolute}

.top-stripe{left:0;top:0;width:960px;height:2px;background:linear-gradient(90deg,#2aa7e0 0 25%,#7b2c8f 25% 50%,#f07f1a 50% 75%,#7cc242 75%)}
.site-header{left:0;top:0;width:960px;height:90px;border-bottom:1px solid #e3e3e3}
.brand{left:146px;top:38px;display:flex;align-items:center;gap:8px}
.brand-mark{width:22px;height:22px;border-radius:50%;background:var(--green)}
.brand-name{font-size:18px;font-weight:600;color:var(--green)}
.partner{left:290px;top:54px;width:100px;height:30px;background:#f5f5f5;font-size:12px;font-weight:600;color:#333;line-height:30px;padding-left:6px}
.nav{top:60px;font-size:10.5px;color:#222}
.nav.active{color:var(--blue)}

.hero{left:0;top:90px;width:960px;height:367px;background:linear-gradient(180deg,#6dba2a 0%,#78c135 55%,#96d257 100%);overflow:hidden}
.hero-glow{left:146px;top:0;width:650px;height:367px;background:radial-gradient(ellipse at 50% 110%,rgba(190,235,140,.8),rgba(190,235,140,0) 70%)}
.video{left:149px;top:55px;width:356px;height:266px;background:linear-gradient(135deg,#e6e3df,#cfc8c0 55%,#b8b1aa);box-shadow:0 2px 6px rgba(0,0,0,.35)}
.play{left:145px;top:103px;width:60px;height:60px;border-radius:50%;background:rgba(226,78,78,.85)}
.login-title{left:548px;top:56px;font-size:17px;color:#fff}
.field-label{left:556px;font-size:10px;color:#fff}
.field{left:611px;width:138px;height:29px;background:var(--field);border:1px solid #cfe6b5}
.btn-signin{left:676px;top:201px;width:73px;height:29px;background:var(--blue);color:#fff;font-size:10px;text-align:center;line-height:29px}
.forgot{left:600px;width:149px;top:244px;text-align:right;font-size:10px;color:#222}

.news{left:145px;top:487px;width:214px;height:363px;border:1px solid var(--rule)}
.news-head{height:55px;background:var(--blue);color:#fff;font-size:16px;padding:17px 0 0 18px}
.news-item{height:102px;border-bottom:1px solid var(--rule);position:relative}
.news-item:last-child{border-bottom:0}
.news-thumb{position:absolute;left:10px;top:20px;width:54px;height:59px;background:linear-gradient(135deg,#e9edf0,#b9c4cc)}
.news-text{position:absolute;left:70px;top:16px;width:140px;font-size:10px;line-height:16.4px;color:#222}
.news-date{color:var(--green-text);font-size:9px;display:block;line-height:13px}

.welcome{left:374px;top:498px;font-size:17px;color:var(--blue)}
.welcome span,.services-title span{color:var(--green-text)}
.intro{left:374px;width:446px;font-size:8.7px;line-height:16.4px;color:var(--muted)}
.services-title{left:374px;top:698px;font-size:17px;color:var(--blue)}
.check{font-size:10px;color:#222;display:flex;align-items:center;gap:4px}
.check svg{width:11px;height:11px}

.site-footer{left:0;top:884px;width:960px;height:237px;background:var(--blue)}
.foot-h{top:26px;font-size:16px;color:#fff}
.map{left:145px;top:66px;width:207px;height:145px;background:linear-gradient(135deg,#ece8de,#dcd6c6)}
.world{left:400px;top:80px;width:170px;height:100px;background:radial-gradient(ellipse,rgba(60,130,210,.45),rgba(60,130,210,0) 70%)}
.contact{left:396px;font-size:10px;color:#fff;line-height:17.6px}
.icon{position:absolute;left:380px}
.nl-text{left:611px;top:58px;width:200px;font-size:8.7px;line-height:20.6px;color:#fff}
.nl-field{left:614px;width:190px;height:28px;background:#fff;font-size:8.5px;color:#888;padding:8px 9px}
.btn-submit{left:614px;top:184px;width:60px;height:27px;background:var(--green);color:#fff;font-size:8.5px;text-align:center;line-height:27px}

.bottom-bar{left:0;top:1121px;width:960px;height:79px;background:var(--blue-dark)}
.legal{left:145px;top:22px;font-size:10px;color:#fff}
.copy{left:145px;top:44px;font-size:8px;color:#dbe6f4}
.social{top:26px;width:28px;height:28px;border-radius:50%;border:2px solid #fff}
</style>
</head>
<body>
<header class="abs site-header">
  <div class="abs top-stripe"></div>
  <div class="abs brand"><span class="brand-mark"></span><span class="brand-name">Vital Beacon</span></div>
  <div class="abs partner">PulseLink</div>
  <a class="abs nav active" style="left:618px">Home</a>
  <a class="abs nav" style="left:682px">Register</a>
  <a class="abs nav" style="left:756px">Contact Us</a>
</header>

<section class="abs hero">
  <div class="abs hero-glow"></div>
  <div class="abs video" role="img" aria-label="Video still: a patient consulting a doctor in a clinic">
    <div class="abs play">
      <svg width="60" height="60" viewBox="0 0 60 60"><path d="M24 19 L42 30 L24 41 Z" fill="#fff"/></svg>
    </div>
  </div>
  <h2 class="abs login-title" style="font-weight:400">Login</h2>
  <label class="abs field-label" style="top:106px">Login ID</label>
  <div class="abs field" style="top:98px"></div>
  <label class="abs field-label" style="top:154px">Password</label>
  <div class="abs field" style="top:146px"></div>
  <div class="abs btn-signin">Sign In</div>
  <div class="abs forgot">Forgot Password?</div>
</section>

<aside class="abs news">
  <div class="news-head">Latest News</div>
  <div class="news-item">
    <div class="news-thumb" role="img" aria-label="News photo: nurse at work"></div>
    <p class="news-text">Lorem ipsum dolor sit amet, consectetuer adipiscing elit, sed diam.<span class="news-date">Jun 22, 2014</span></p>
  </div>
  <div class="news-item">
    <div class="news-thumb" role="img" aria-label="News photo: smiling senior patient"></div>
    <p class="news-text">Ut wisi enim ad minim veniam, quis nostrud exerci tation ullamcorper suscipit lobortis<span class="news-date">Jun 22, 2014</span></p>
  </div>
  <div class="news-item">
    <div class="news-thumb" role="img" aria-label="News photo: doctor with a patient"></div>
    <p class="news-text">Claritas est etiam processus dynamicus, qui sequitur mut ationem consuetudium..<span class="news-date">Jun 22, 2014</span></p>
  </div>
</aside>

<h1 class="abs welcome" style="font-weight:400">Welcome To <span>Vital Beacon</span></h1>
<p class="abs intro" style="top:529px">Typi non habent claritatem insitam; est usus legentis in iis qui facit eorum claritatem. Investigationes demonstraverunt lectores legere me lius quod ii legunt saepius. Claritas est etiam processus dynamicus, qui sequitur mutationem consuetudium lectorum. Mirum est notare quam littera gothica, quam nunc putamus parum claram, anteposuerit litterarum formas humanitatis per seacula quarta decima et quinta decima. Eodem modo typi, qui nunc nobis videntur parum clari, fiant sollemnes in futurum.</p>
<p class="abs intro" style="top:617px">Legere me lius quod ii legunt saepius. Claritas est etiam processus dynamicus, qui sequitur mutationem consuetudium lectorum. Mirum est notare quam littera gothica, quam nunc putamus parum claram, anteposuerit litterarum formas humanitatis per seacula quarta decima et quinta decima. Eodem modo typi, qui nunc nobis videntur parum clari, fiant sollemnes in futurum.</p>

<h2 class="abs services-title" style="font-weight:400">Our <span>Services</span></h2>
<svg width="0" height="0" style="position:absolute"><symbol id="tick" viewBox="0 0 12 12"><rect x=".5" y=".5" width="11" height="11" fill="#fff" stroke="#ddd"/><path d="M3 6.2 L5.2 8.3 L9.3 3.5" fill="none" stroke="#5aad1f" stroke-width="1.6"/></symbol></svg>
<div class="abs check" style="left:400px;top:740px"><svg><use href="#tick"/></svg>Lorem ipsum dolor sit</div>
<div class="abs check" style="left:400px;top:770px"><svg><use href="#tick"/></svg>Typi non habent claritatem insitam</div>
<div class="abs check" style="left:400px;top:800px"><svg><use href="#tick"/></svg>Eodem modo typi, qui nunc nobis</div>
<div class="abs check" style="left:400px;top:830px"><svg><use href="#tick"/></svg>Ut wisi enim ad minim</div>
<div class="abs check" style="left:622px;top:740px"><svg><use href="#tick"/></svg>Eodem modo typi, qui nunc nobis</div>
<div class="abs check" style="left:622px;top:770px"><svg><use href="#tick"/></svg>Lorem ipsum dolor sit</div>
<div class="abs check" style="left:622px;top:800px"><svg><use href="#tick"/></svg>Typi non habent claritatem insitam</div>
<div class="abs check" style="left:622px;top:830px"><svg><use href="#tick"/></svg>Ut wisi enim ad minim</div>

<footer class="abs site-footer">
  <h3 class="abs foot-h" style="left:145px;font-weight:400">Our Location</h3>
  <div class="abs map" role="img" aria-label="Street map showing the office location"></div>

  <h3 class="abs foot-h" style="left:377px;font-weight:400">Get In Touch</h3>
  <div class="abs world" role="img" aria-label="Faint world map backdrop"></div>
  <svg class="icon" style="top:82px" width="10" height="14" viewBox="0 0 10 14"><path d="M5 0a5 5 0 0 0-5 5c0 4 5 9 5 9s5-5 5-9a5 5 0 0 0-5-5zm0 7a2 2 0 1 1 0-4 2 2 0 0 1 0 4z" fill="#fff"/></svg>
  <div class="abs contact" style="top:84px">Lorem Ipsm, Lorem Ipsm<br>Lorem Ipsm -123 456</div>
  <svg class="icon" style="top:131px" width="12" height="12" viewBox="0 0 12 12"><path d="M2.5 0.5 L4.5 3 L3.4 4.4 C4.2 6 5.9 7.7 7.6 8.6 L9 7.5 L11.5 9.5 L10 11.5 C5 11 1 7 0.5 2 Z" fill="#fff"/></svg>
  <div class="abs contact" style="top:130px">123 456 (789) 000</div>
  <svg class="icon" style="top:171px" width="12" height="9" viewBox="0 0 12 9"><rect x=".5" y=".5" width="11" height="8" fill="none" stroke="#fff"/><path d="M.5 .5 L6 5 L11.5 .5" fill="none" stroke="#fff"/></svg>
  <div class="abs contact" style="top:167px">hello@vitalbeacon.test</div>

  <h3 class="abs foot-h" style="left:610px;font-weight:400">Newsletter Signup</h3>
  <p class="abs nl-text">Lorem ipsum dolor sit amet, consectetuer adipiscing elit, volutpat.</p>
  <div class="abs nl-field" style="top:102px">Name</div>
  <div class="abs nl-field" style="top:142px">Email Address</div>
  <div class="abs btn-submit">SUBMIT</div>
</footer>

<div class="abs bottom-bar">
  <div class="abs legal">Privacy &amp; policy &nbsp;&nbsp;|&nbsp;&nbsp; Sitemap</div>
  <div class="abs copy">Copyrights@2014 Vital Beacon. All Right Reserved.</div>
  <span class="abs social" style="left:649px;background:#3b5b98"></span>
  <span class="abs social" style="left:684px;background:#2aa3e0"></span>
  <span class="abs social" style="left:718px;background:#c4302b"></span>
  <span class="abs social" style="left:752px;background:#d2442f"></span>
  <span class="abs social" style="left:787px;background:#f26a1b"></span>
</div>
</body>
</html>
```